Harrowby Wine Label - Design a front and smaller back label for an exclusive red wine

Harrowby Wines produces a very high quality, high priced wine from an old and prestigous vineyard in one of Australia's oldest, but smallest wine growing regions. The grapevines are old (like old men with gnarled arms and trunks) and they produce fewer grapes than younger vines but the grape quality (and thus wine quality) is magnificent and highly sought after as it produces wine of exceptional quality.
The vineyard was purchased by the Harrowby family in February 2010 from a multinational wine company who made wonderful, trophy winning wines for 10 years before the vineyard went into a decline.
The challenge is to produce 2 labels - a simple main front label that focuses on the Harrowby brand and a smaller, information rich, back label that relates the history of the vineyard.
The labels should have a white or charcoal grey background and impart tradition, quality, exclusivity and a little self indulgence which is why we want the family crest incorporated - the choice of font will help.
It might also impart a sense of fun so that it appeals to the 25-35 year old age bracket.
The label should be kept clean and simple not loud and busy. Preferred colours are black, grey and white. Red is fine if used sparingly

Here are the details:_

Front Label (115 long x 65-90mm wide)

Harrowby
Lanternwatch Reserve
2011
Mudgee
Wine of Australia 750ml

Back Label (dimensions to suit text and front label design; font size small; text in black so that it is readable in less than optimal light (eg candlelight at a restaurant table).

Harrowby
Lanternwatch Reserve 2011

This is the first release of The Lanternwatch’s Reserve – just 100 dozen bottles were made. The wine was made from Shiraz and 10% Cabernet Sauvignon grapes sourced from an iconic Mudgee vineyard that was established 1966 by Peter Vallis. In 1994, the vineyard known as ”Silver Hollow”, became the source of a decade of formidable, trophy winning wines under Tindalberg’s and later Quellwood’s ownership. The 20ha vineyard was purchased by Corin & Margaret Harrowby in 2010. The Silver Hollow name was retained by Quellwoods; no wine has been released under this label since the 2006 vintage.

The shaky old Shiraz vines are slowly being restored to full health using careful cane pruning techniques that stimulates fresh, new tissue growth, more even bunch sizes and better grape quality and consistency. The Shiraz grapes used in this wine were hand-picked from two rows of the first crop from the 46 year old, cane pruned vines. The 2011 Reserve is the first step to re-establish the traditions of a famous vineyard and one of Australia’s most sought after export wines.

“Deep and intense purple hues with aromas of ripe blackberry fruits, spice and eucalypt with rich chocolate complemented by subtle oak overtones. A rich and full bodied wine exhibiting a soft yet generous palate with plum, forest fruits and mint chocolate notes. A fine grained tannin structure displaying integrated oak characters adds to the complexity of the wine. This wine was aged for 18 months in a blend of new French oak hogsheads and one year old American hogsheads, crafting a blend with great structure and length of flavour which will develop into a Mudgee classic” – Lewis Farrant, Winemaker

13.5% Alc/Vol.
Contains approx 8.0 std drinks
Preservative (220) added

Harrowby Wines
Tallowbend Rd, Mudgee 2850
www.harrowbywines.example.au

Reason: My apologies to the designers who have kindly submitted some wonderful designs. I am trying to achieve a conscentious between shareholders. This is difficult as they are in different parts of the world and I have learned through this experience that opinions on wine labels are quite diverse!!! The feedback I have received so far indicates the following (1) A light or white background is preferred (2) The crest should not be a dominant part of the label (3) The label needs to be clean, fresh and uncomplicated (4) If red is used it should be in minor detail only (5) "Harrowby" should be distinctive. The font is difficult for us! (6) We are considering "The Lanternwatch" RESERVE instead of "Lanternwatch's" RESERVE (7) The text on the back label is too long; I will edit and re-upload Many thanks for your help and patience Kind regards Corin

Good Morning All,
I have edited the back label text to reduce the size of the label. A Word file with the changes has just been uploaded.
Cheers
Corin

Dear Designers,
Thank you all so very much for the wonderful selection of designs you have submitted my family have all been overwhelmed by the quality and skill level exhibited and we all appreciate you your efforts
Kindest regards
Corin

Target Market(s)

25-35 year old men and women of Australia, China, US & UK

Industry/Entity Type

Restaurant

Requirements
Must have
• Crest
Should not have
• Animals on the label

```html
<!DOCTYPE html>
<html lang="en">
<head>
<meta charset="utf-8">
<title>Harrowby Lanternwatch's Reserve – Front and Back Labels</title>
<link rel="stylesheet" href="https://fonts.googleapis.com/css2?family=Roboto+Condensed:wght@300;400;700&family=Roboto:wght@400;700&display=swap">
<style>
  :root {
    --paper: #e6e3d2;
    --brick: #c24f39;
    --brick-soft: #cf6a55;
    --ink: #2d2d2d;
    --ink-soft: #3a3a3a;
    --page: #ffffff;
    --cream-text: #f3eee2;
  }
  * { box-sizing: border-box; margin: 0; padding: 0; }
  html, body {
    width: 1200px; height: 900px; overflow: hidden;
    background: var(--page);
    font-family: "Roboto Condensed", "Arial Narrow", sans-serif;
    color: var(--ink);
  }
  .stage { position: relative; width: 1200px; height: 900px; }

  .label {
    position: absolute; top: 262px;
    width: 277px; height: 490px;
    background: var(--paper);
    box-shadow: 0 1px 4px rgba(0,0,0,.18);
    overflow: hidden;
  }
  .label--front { left: 307px; }
  .label--back  { left: 617px; }

  .label__red {
    position: absolute; left: 0; right: 0; bottom: 0;
    background: var(--brick);
  }
  .label--front .label__red { top: 272px; }
  .label--back  .label__red { top: 392px; }
  .label__teeth {
    position: absolute; left: 0; top: -7px; width: 277px; height: 7px; display: block;
  }
  .label__frame {
    position: absolute; inset: 9px;
    border: 1.5px solid var(--ink);
    pointer-events: none;
  }

  /* Front label */
  .brand-name {
    position: absolute; top: 34px; left: 0; right: 0;
    text-align: center;
    font-weight: 700; font-size: 17px; letter-spacing: 3px;
    color: var(--brick);
  }
  .vintage {
    position: absolute; top: 60px; left: 0; right: 0;
    display: flex; justify-content: center; align-items: center; gap: 14px;
    font-family: "Roboto", sans-serif; font-weight: 700; font-size: 27px;
    color: var(--ink);
  }
  .vintage__dot {
    width: 88px; height: 88px; border-radius: 50%;
    background: var(--ink-soft);
  }
  .reserve-name {
    position: absolute; top: 156px; left: 0; right: 0;
    text-align: center;
    font-size: 13px; letter-spacing: 2.4px; text-transform: uppercase;
    color: var(--brick);
  }
  .region {
    position: absolute; top: 217px; left: 0; right: 0;
    text-align: center;
    font-family: "Roboto", sans-serif; font-weight: 700; font-size: 15px;
  }
  .origin {
    position: absolute; top: 239px; left: 0; right: 0;
    text-align: center;
    font-family: "Roboto", sans-serif; font-size: 12.5px; letter-spacing: .3px;
  }
  .crest {
    position: absolute; left: 96px; top: 40px;
    width: 86px; height: 118px;
    border-radius: 4px 4px 40px 40px;
    background: var(--brick-soft);
  }
  .volume {
    position: absolute; left: 0; right: 0; top: 178px;
    text-align: center;
    font-family: "Roboto", sans-serif; font-weight: 700; font-size: 11px;
    color: var(--cream-text);
  }

  /* Back label */
  .back__brand {
    position: absolute; top: 21px; left: 0; right: 0;
    text-align: center;
    font-weight: 700; font-size: 12px; letter-spacing: 2.6px;
  }
  .back__title {
    position: absolute; top: 35px; left: 16px; right: 16px;
    text-align: center; white-space: nowrap;
    font-weight: 300; font-size: 18.5px; letter-spacing: 1px;
  }
  .back__year {
    position: absolute; top: 57px; left: 18px; right: 18px;
    display: flex; align-items: center; gap: 6px;
    font-size: 10px; letter-spacing: 1px;
  }
  .back__year::before, .back__year::after {
    content: ""; flex: 1; border-top: 1px solid var(--ink);
  }
  .back__story {
    position: absolute; top: 74px; left: 16px; right: 16px; height: 308px;
    columns: 2; column-gap: 11px; column-fill: auto;
    font-size: 8.5px; line-height: 10.5px; letter-spacing: -0.1px;
    text-align: justify; color: var(--ink);
  }
  .back__story p + p { margin-top: 10.5px; }

  .back__facts {
    position: absolute; top: 9px; left: 0; right: 0;
    text-align: center;
    font-family: "Roboto", sans-serif; font-size: 10px; line-height: 12px;
    color: var(--cream-text);
  }
  .back__maker {
    position: absolute; top: 36px; left: 20px; right: 20px;
    display: flex; align-items: center; justify-content: space-between;
  }
  .back__ornament {
    width: 62px; height: 16px; border-radius: 8px;
    background: var(--brick-soft);
  }
  .back__maker-name {
    font-size: 17px; letter-spacing: 2px; color: var(--cream-text);
  }
  .back__address {
    position: absolute; top: 61px; left: 0; right: 0;
    text-align: center;
    font-family: "Roboto", sans-serif; font-size: 10px;
    color: var(--cream-text);
  }
  .back__web {
    position: absolute; top: 75px; left: 0; right: 0;
    text-align: center;
    font-family: "Roboto", sans-serif; font-weight: 700; font-size: 8.5px; letter-spacing: .6px;
    color: var(--cream-text);
  }
</style>
</head>
<body>
<main class="stage">

  <svg width="0" height="0" style="position:absolute" aria-hidden="true">
    <defs>
      <pattern id="zigzag" width="11" height="7" patternUnits="userSpaceOnUse">
        <polygon points="0,7 5.5,0 11,7" fill="#c24f39"/>
      </pattern>
    </defs>
  </svg>

  <section class="label label--front" aria-label="Front label">
    <div class="brand-name">HARROWBY</div>
    <div class="vintage">
      <span>20</span>
      <span class="vintage__dot"></span>
      <span>11</span>
    </div>
    <div class="reserve-name">Lanternwatch's Reserve</div>
    <div class="region">Mudgee</div>
    <div class="origin">Wine of Australia</div>

    <div class="label__red">
      <svg class="label__teeth" viewBox="0 0 277 7" preserveAspectRatio="none" aria-hidden="true">
        <rect width="277" height="7" fill="url(#zigzag)"/>
      </svg>
      <div class="crest" role="img" aria-label="Harrowby family crest"></div>
      <div class="volume">750ml</div>
    </div>
    <div class="label__frame"></div>
  </section>

  <section class="label label--back" aria-label="Back label">
    <div class="back__brand">HARROWBY</div>
    <div class="back__title">LANTERNWATCH'S RESERVE</div>
    <div class="back__year">2011</div>

    <div class="back__story">
      <p>This is the first release of the Lanternwatch's Reserve – just 100 dozen bottles were made. The wine was made from Shiraz and 10% Cabernet Sauvignon grapes sourced from an iconic Mudgee vineyard that was established 1966 by Peter Vallis. In 1994, the vineyard known as ”Silver Hollow”, became the source of a decade of formidable, trophy winning wines under Tindalberg’s and later Quellwood’s ownership. The 20ha vineyard was purchased by Corin &amp; Margaret Harrowby in 2010. The Silver Hollow name was retained by Quellwoods; no wine has been released under this label since the 2006 vintage.</p>
      <p>The shaky old Shiraz vines are slowly being restored to full health using careful cane pruning techniques that stimulates fresh, new tissue growth, more even bunch sizes and better grape quality and consistency. The Shiraz grapes used in this wine were hand-picked from two rows of the first crop from the 46 year old, cane pruned vines. The 2011 Reserve is the first step to re-establish the traditions of a famous vineyard and one of Australia’s most sought after export wines.</p>
      <p>“Deep and intense purple hues with aromas of ripe blackberry fruits, spice and eucalypt with rich chocolate complemented by subtle oak overtones. A rich and full bodied wine exhibiting a soft yet generous palate with plum, forest fruits and mint chocolate notes. A fine grained tannin structure displaying integrated oak characters adds to the complexity of the wine. This wine was aged for 18 months in a blend of new French oak hogsheads and one year old American hogsheads, crafting a blend with great structure and length of flavour which will develop into a Mudgee classic” – Lewis Farrant, Winemaker</p>
    </div>

    <div class="label__red">
      <svg class="label__teeth" viewBox="0 0 277 7" preserveAspectRatio="none" aria-hidden="true">
        <rect width="277" height="7" fill="url(#zigzag)"/>
      </svg>
      <div class="back__facts">13.5% Alc/Vol. Contains approx 8.0 std drinks<br>Preservative (220) added</div>
      <div class="back__maker">
        <span class="back__ornament" role="img" aria-label="Decorative ornament"></span>
        <span class="back__maker-name">HARROWBY</span>
        <span class="back__ornament" role="img" aria-label="Decorative ornament"></span>
      </div>
      <div class="back__address">Harrowby Wines Tallowbend Rd, Mudgee 2850</div>
      <div class="back__web">www.harrowbywines.example.au</div>
    </div>
    <div class="label__frame"></div>
  </section>

</main>
</body>
</html>
```